Design my dad a new business card because his current one sucks!

I need a business card designed for my fathers home maintenance business. His customers are individuals (single moms, old people etc.) as well as the occasional business. As such it needs to be accessible to both target audiences.

The front of the card should be dark grey on yellow with the logo and contain the following information:
- Warren Dobrinski
- 0487 362 914
- info@harbourlinehandyworks.com.au
- 0487 362 914

- ABN: 87 214 630 592
- 'Fully Insured'

The reverse should be yellow on dark grey and will have the web address:
- harbourlinehandyworks.com.au

And a few key services he offers:
GENERAL REPAIRS
PAINTING/TILING/
PAVING &CONCRETING
PRESSURE WASHING
ON-SITE WELDING
DECKING ADDITIONS & REPAIRS
FENCING
FULL BOND CLEANING

This will be first time the logo has been printed so you will need to come up with the best CMYK approximation of the RGB colours to make sure it is a close as possible.

```html
<!DOCTYPE html>
<html lang="en">
<head>
<meta charset="utf-8">
<title>Harbourline Handyworks – Business Card</title>
<link rel="stylesheet" href="https://fonts.googleapis.com/css2?family=Montserrat:wght@600;800&family=Open+Sans:wght@400;600&display=swap">
<style>
  :root {
    --yellow: #f7dc14;
    --yellow-deep: #f2c400;
    --charcoal: #3a3a3c;
    --card-dark: #2b2b2d;
    --ink-on-yellow: #474747;
    --backdrop: #ece9e2;
  }
  * { box-sizing: border-box; margin: 0; padding: 0; }
  html, body {
    width: 1200px; height: 913px; overflow: hidden;
    background: var(--backdrop);
  }
  .canvas {
    position: relative; width: 1200px; height: 913px;
    display: flex; align-items: center; justify-content: center; gap: 60px;
  }
  .card {
    width: 520px; height: 300px; border-radius: 6px;
    position: relative; overflow: hidden;
    box-shadow: 0 10px 30px rgba(0,0,0,.18);
  }

  /* Yellow side */
  .card--front {
    background: linear-gradient(135deg, var(--yellow) 0%, var(--yellow-deep) 100%);
    color: var(--ink-on-yellow);
    display: flex; flex-direction: column; align-items: center; justify-content: center;
  }
  .brand {
    font-family: "Montserrat", sans-serif; font-weight: 800;
    display: flex; align-items: center; gap: 10px;
    white-space: nowrap;
  }
  .brand__mark { width: 18px; height: 18px; border-radius: 50%; background: currentColor; flex: none; }
  .card--front .brand { font-size: 28px; letter-spacing: .3px; }
  .card--front .web {
    margin-top: 40px;
    font-family: "Open Sans", sans-serif; font-weight: 600; font-size: 16px;
  }

  /* Charcoal side */
  .card--back {
    background: linear-gradient(135deg, var(--charcoal) 0%, var(--card-dark) 100%);
    color: var(--yellow);
    font-family: "Open Sans", sans-serif;
  }
  .card--back .brand {
    position: absolute; left: 24px; bottom: 28px;
    font-size: 19px; flex-direction: column; align-items: flex-start; gap: 6px;
    line-height: 1.1;
  }
  .card--back .brand__mark { width: 14px; height: 14px; }
  .top-rule {
    position: absolute; left: 212px; right: 0; top: 20px;
    height: 1px; background: var(--yellow); opacity: .6;
  }
  .contact {
    position: absolute; left: 212px; top: 30px; right: 20px;
    white-space: nowrap;
  }
  .contact__name { font-size: 19px; font-weight: 400; line-height: 25px; }
  .contact__role { font-size: 12px; line-height: 16px; margin-bottom: 10px; }
  .contact__lines { font-size: 11px; font-weight: 600; line-height: 17px; }
  .rule { height: 1px; background: var(--yellow); opacity: .7; margin: 10px 0 9px; }
  .services {
    list-style: none; font-size: 10px; font-weight: 600;
    line-height: 16px; letter-spacing: .2px;
  }
  .services .dot { margin: 0 5px; }
  .insured {
    position: absolute; right: 22px; bottom: 18px;
    font-size: 15px; line-height: 20px;
  }
</style>
</head>
<body>
<main class="canvas">
  <section class="card card--front" aria-label="Card front">
    <div class="brand"><span class="brand__mark"></span>Harbourline Handyworks</div>
    <p class="web">www.harbourlinehandyworks.com.au</p>
  </section>

  <section class="card card--back" aria-label="Card back">
    <div class="top-rule"></div>
    <div class="brand"><span class="brand__mark"></span>Harbourline<br>Handyworks</div>
    <div class="contact">
      <p class="contact__name">Warren Dobrinski</p>
      <p class="contact__role">owner</p>
      <div class="contact__lines">
        <p>Ph: 0487 362 914</p>
        <p>Email: info@harbourlinehandyworks.com.au</p>
        <p>ABN: 87 214 630 592</p>
      </div>
      <div class="rule"></div>
      <ul class="services">
        <li>GENERAL REPAIRS<span class="dot">•</span>PAINTING/TILING/</li>
        <li>PAVING &amp; CONCRETING<span class="dot">•</span>PRESSURE WASHING</li>
        <li>ON-SITE WELDING<span class="dot">•</span>DECKING ADDITIONS &amp; REPAIRS</li>
        <li>FENCING<span class="dot">•</span>FULL BOND CLEANING</li>
      </ul>
    </div>
    <p class="insured">Fully Insured</p>
  </section>
</main>
</body>
</html>
```